North Little Rock (by the numbers)

We (city communications office of North Little Rock, Arkansas) are launching a magazine to be delivered to every house in the community. We would like the first inside page to be an infographic of the important and interesting "numbers" from 2017. We want it to be visually interesting and convey the huge amount of important services we provide our residents. I have included a document with the relevant statistics to be used.

Target Market(s)

Residents of our city

Industry/Entity Type

House

Colors

Designer to choose colors to be used in the design.

Requirements
Must have
• Our logo must be prominent. The dimensions should be able to fit onto a standard full page magazine. If the infographic is best displayed on two pages we will accept that as well, and change our layout.
Nice to have
• Not every statistic we have provided must be used but if they can be, that is preferable. I have also included some inspirational infographics that appealed to me and inspired the idea, but I am excited about new concepts that might not look anything like those that I have provided.
Should not have
• The design should not have anything incorporated that cannot be presented to families in our community. It must be all ages friendly.

```html
<!DOCTYPE html>
<html lang="en">
<head>
<meta charset="utf-8">
<title>Cedar Ridge Falls by the Numbers 2017</title>
<link rel="stylesheet" href="https://fonts.googleapis.com/css2?family=Arimo:wght@400;700&display=swap">
<style>
  :root {
    --navy: #1f3a4d;
    --ink: #2b2b2b;
    --muted: #333333;
    --red: #e42a2e;
    --red-deep: #c8212a;
    --police: #1b2a5a;
    --green: #6cb33f;
    --brown: #6b4a1f;
    --brown-text: #7a5322;
    --asphalt: #5f6569;
    --white: #ffffff;
    --dash: #4a4a4a;
  }
  * { box-sizing: border-box; margin: 0; padding: 0; }
  html, body { width: 1200px; height: 3734px; overflow: hidden; background: var(--white); }
  body { font-family: "Arimo", Arial, sans-serif; color: var(--ink); }
  .page { position: relative; width: 1200px; height: 3734px; overflow: hidden; background: var(--white); }
  .abs { position: absolute; }

  /* Header scene */
  .skyline { left: 0; top: 0; width: 1200px; height: 456px;
    background: linear-gradient(180deg, #3aa6df 0%, #6cc1ea 35%, #f0b640 62%, #e9dcc2 82%, #f2ece0 100%); }
  .skyline-base { left: 0; top: 452px; width: 1200px; height: 14px; background: var(--navy); }
  .title-banner { left: 300px; top: 55px; width: 900px; height: 100px; background: var(--navy);
    clip-path: polygon(6% 0, 100% 0, 100% 100%, 6% 100%, 0 50%);
    color: var(--white); font-weight: 700; font-size: 52px; display: flex; align-items: center; justify-content: flex-end; padding-right: 26px; white-space: nowrap; }
  .year-badge { left: 748px; top: 155px; width: 298px; height: 88px; background: var(--white);
    border: 6px solid var(--navy); border-top: none;
    font-weight: 700; font-size: 78px; color: var(--navy); display: flex; align-items: center; justify-content: center; }

  /* Population */
  .crowd { left: 0; top: 423px; width: 475px; height: 350px;
    background: linear-gradient(180deg, #f1c8a3 0%, #e07a4a 30%, #3d8fb8 60%, #2b3d5a 100%); border-radius: 0 0 70px 0; }
  .population-label { left: 568px; top: 538px; font-size: 55px; color: var(--ink); }
  .population-ribbon { left: 485px; top: 610px; width: 523px; height: 106px; background: var(--red);
    clip-path: polygon(7% 0, 100% 0, 89% 50%, 100% 100%, 0 100%);
    color: var(--white); font-weight: 700; font-size: 70px; display: flex; align-items: center; padding-left: 62px; }

  /* Park */
  .park-scene { left: 540px; top: 760px; width: 660px; height: 280px;
    background: linear-gradient(180deg, rgba(255,255,255,0) 0%, #a8d67a 45%, #4f9a2e 100%); border-radius: 160px 0 0 0; }
  .park-label { left: 122px; top: 850px; font-size: 51px; color: var(--ink); white-space: nowrap; }
  .park-ribbon { left: 0; top: 958px; width: 470px; height: 82px; background: var(--green);
    clip-path: polygon(0 0, 100% 0, 94% 50%, 100% 100%, 0 100%);
    color: var(--white); font-weight: 700; font-size: 68px; display: flex; align-items: center; padding-left: 60px; }

  /* Emergency */
  .emergency { top: 1095px; width: 460px; height: 300px; }
  .emergency.police { left: 75px; }
  .emergency.fire { left: 690px; }
  .service-tag { position: absolute; left: 0; top: 0; height: 82px; color: var(--white);
    font-size: 66px; display: flex; align-items: center; justify-content: center; }
  .police .service-tag { width: 312px; background: var(--police); }
  .fire .service-tag { width: 306px; background: var(--red-deep); letter-spacing: 24px; padding-left: 24px; }
  .calls-label { position: absolute; left: 12px; top: 92px; font-weight: 700; font-size: 56px; color: var(--ink); white-space: nowrap; }
  .calls-count { position: absolute; left: 10px; top: 152px; font-weight: 700; font-size: 80px; color: var(--red-deep); }
  .responder { position: absolute; top: -12px; width: 125px; height: 237px; border-radius: 44px 44px 16px 16px;
    background: linear-gradient(180deg, #2a3f7d 0%, #f2c39c 22%, #2c3f7a 40%, #1d2a55 100%); }
  .police .responder { left: 323px; }
  .fire .responder { left: 306px; width: 150px;
    background: linear-gradient(180deg, #e5392c 0%, #f2c39c 24%, #e0862a 42%, #9a6a3a 100%); }

  .divider { left: 40px; width: 1120px; height: 0; border-top: 5px dashed var(--dash); }

  .stat-text { font-size: 47px; line-height: 1.3; color: var(--muted); white-space: nowrap; }
  .stat-number { font-weight: 700; font-size: 76px; color: var(--ink); }
  .right { text-align: right; }

  .ph-dozer { left: 722px; top: 1494px; width: 373px; height: 186px; border-radius: 30px 30px 60px 60px;
    background: linear-gradient(180deg, #27b0e8 0%, #f5c518 30%, #f5c518 65%, #2e2e2e 100%); }
  .ph-bags { left: 150px; top: 1855px; width: 286px; height: 200px; border-radius: 50% 50% 30px 30px;
    background: linear-gradient(180deg, #3a3a3a 0%, #1e1e1e 75%, #c9dbe6 100%); }
  .ph-bin { left: 785px; top: 2216px; width: 323px; height: 212px; border-radius: 16px;
    background: linear-gradient(180deg, #eeeeee 0%, #cfcfcf 50%, #5a7fb0 78%, #7a4a32 100%); }
  .ph-truck { left: 105px; top: 2602px; width: 368px; height: 174px; border-radius: 20px;
    background: linear-gradient(180deg, #3ea24d 0%, #2a7a37 70%, #2d2d2d 100%); }

  /* Neighborhood parks */
  .chevron { top: 2922px; width: 105px; height: 105px; }
  .parks-row { left: 190px; top: 2922px; width: 820px; height: 105px; display: flex; align-items: center; justify-content: center; white-space: nowrap; }
  .parks-row .label { font-size: 55px; color: var(--brown-text); }
  .parks-row .count { font-weight: 700; font-size: 76px; color: var(--brown-text); margin-left: 16px; }

  /* Inclusive playground */
  .inclusive-band { left: 0; top: 3057px; width: 1200px; height: 292px; background: var(--red); }
  .inclusive-text { left: 130px; top: 3080px; font-size: 55px; line-height: 75px; color: var(--white); white-space: nowrap; }
  .inclusive-badge { left: 991px; top: 3125px; width: 150px; height: 150px; border-radius: 50%;
    background: var(--white); color: var(--red); font-weight: 700; font-size: 104px;
    display: flex; align-items: center; justify-content: center; }

  /* Footer */
  .landscape { left: 0; top: 3349px; width: 1200px; height: 162px;
    background: linear-gradient(180deg, #ffffff 0%, #9ccf5e 45%, #3e9a36 100%); }
  .fence-band { left: 0; top: 3511px; width: 1200px; height: 40px;
    background: linear-gradient(180deg, #7cc043 0%, #e7d84a 100%); }
  .road { left: 0; top: 3551px; width: 1200px; height: 183px; background: var(--asphalt); }
  .road-edge { left: 0; top: 3551px; width: 1200px; height: 10px; background: #4b5054; }
</style>
</head>
<body>
<main class="page">

  <header>
    <div class="abs skyline" role="img" aria-label="City skyline scene: blue sky, clouds, a tall gold tower, domed civic hall, red arch bridge and colourful office blocks"></div>
    <div class="abs skyline-base"></div>
    <h1 class="abs title-banner">Cedar Ridge Falls (CRF)</h1>
    <div class="abs year-badge">2017</div>
  </header>

  <section class="population">
    <div class="abs crowd" role="img" aria-label="Crowd of residents in colourful clothing"></div>
    <p class="abs population-label">Population</p>
    <div class="abs population-ribbon">65,004</div>
  </section>

  <section class="park-visitors">
    <div class="abs park-scene" role="img" aria-label="Park scene with green trees, bushes, a bench and a litter bin"></div>
    <p class="abs park-label">Visitors to Riverbend Park</p>
    <div class="abs park-ribbon">779,621</div>
  </section>

  <section class="abs emergency police">
    <div class="service-tag">POLICE</div>
    <p class="calls-label">911 calls</p>
    <p class="calls-count">26,660</p>
    <div class="responder" role="img" aria-label="Police officer in blue uniform"></div>
  </section>

  <section class="abs emergency fire">
    <div class="service-tag">FIRE</div>
    <p class="calls-label">911 calls</p>
    <p class="calls-count">12,560</p>
    <div class="responder" role="img" aria-label="Firefighter in helmet and turnout gear"></div>
  </section>

  <div class="abs divider" style="top:1400px"></div>

  <section class="stat asphalt">
    <p class="abs stat-text" style="left:70px;top:1428px">Tons of asphalt used in<br>repairing potholes and<br>street overlays</p>
    <p class="abs stat-number" style="left:70px;top:1618px">5,952</p>
    <div class="abs ph-dozer" role="img" aria-label="Yellow bulldozer"></div>
  </section>

  <div class="abs divider" style="top:1770px"></div>

  <section class="stat garbage">
    <div class="abs ph-bags" role="img" aria-label="Black bags of household garbage with litter"></div>
    <p class="abs stat-text right" style="right:60px;top:1840px">Tons of Household<br>garbage collected</p>
    <p class="abs stat-number right" style="right:60px;top:1966px">16,768</p>
  </section>

  <div class="abs divider" style="top:2138px"></div>

  <section class="stat tires">
    <p class="abs stat-text" style="left:70px;top:2248px">Used tires recycled</p>
    <p class="abs stat-number" style="left:70px;top:2305px">4,221</p>
    <div class="abs ph-bin" role="img" aria-label="Wire recycling basket with scattered items"></div>
  </section>

  <div class="abs divider" style="top:2505px"></div>

  <section class="stat green-waste">
    <div class="abs ph-truck" role="img" aria-label="Green waste collection truck"></div>
    <p class="abs stat-text right" style="right:60px;top:2584px">Cubic yards of green<br>(yard) waste collected</p>
    <p class="abs stat-number right" style="right:60px;top:2706px">116,675</p>
  </section>

  <div class="abs divider" style="top:2873px"></div>

  <section class="neighborhood-parks">
    <svg class="abs chevron" style="left:70px" viewBox="0 0 100 100" aria-hidden="true">
      <polygon points="0,0 100,50 0,100 30,50" fill="var(--brown)"/>
    </svg>
    <div class="abs parks-row"><span class="label">Neighborhood parks</span><span class="count">– 34</span></div>
    <svg class="abs chevron" style="left:1026px" viewBox="0 0 100 100" aria-hidden="true">
      <polygon points="100,0 0,50 100,100 70,50" fill="var(--brown)"/>
    </svg>
  </section>

  <section class="inclusive">
    <div class="abs inclusive-band"></div>
    <p class="abs inclusive-text">Kind Circle Inclusive<br>Playgrounds built for kids<br>with special needs</p>
    <div class="abs inclusive-badge">1</div>
  </section>

  <footer>
    <div class="abs landscape" role="img" aria-label="Green hills with rows of trees"></div>
    <div class="abs fence-band" role="img" aria-label="Low yellow roadside fence"></div>
    <div class="abs road"></div>
    <div class="abs road-edge"></div>
    <svg class="abs" style="left:0;top:3662px" width="1200" height="20" viewBox="0 0 1200 20" aria-hidden="true">
      <rect x="0" y="5" width="112" height="10" fill="#fff"/>
      <rect x="294" y="5" width="192" height="10" fill="#fff"/>
      <rect x="710" y="5" width="186" height="10" fill="#fff"/>
      <rect x="1096" y="5" width="104" height="10" fill="#fff"/>
    </svg>
  </footer>

</main>
</body>
</html>
```